BRIXLEY ELECTRICAL

all black background with silver and lime writing, fonts i like are gothic style but am open to ideas, will need a picture logo aswell as im putting this on my van.i am a electrical contractor starting up my own electrical business. underneath brixley electrical heading on card we could put" professiona cost effective soloutions to all your electrical needs".{ or something of that nature }.on aback of card on top half list servises provided, real estate and commercial maintenance, new home and renovation rewires and upgrades, split system air conditioning, floor heat, tv phone data, smoke detoctors, lighting systems , builders welcome, , and also a thankyou for your business.

Industry/Entity Type

Real Estate

Contact Information for Business Card

GAVIN PRESTWORTH
brixleyelectrical@quillnet.com.au
0417352940
lic no 81926
ac lic no l593721
abn 37216405813

```html
<!DOCTYPE html>
<html lang="en">
<head>
<meta charset="utf-8">
<title>Brixley Electrical – Card Back</title>
<link rel="stylesheet" href="https://fonts.googleapis.com/css2?family=Saira:wght@400;700&display=swap">
<style>
  :root {
    --ink: #000000;
    --lime: #a9c93b;
    --frame: #3a3a3a;
    --mark-tone: #161616;
  }
  * { margin: 0; padding: 0; box-sizing: border-box; }
  html, body {
    width: 1200px;
    height: 740px;
    overflow: hidden;
    background: var(--ink);
  }
  .card-back {
    position: relative;
    width: 1200px;
    height: 740px;
    background: var(--ink);
    border: 1px solid var(--frame);
    font-family: "Saira", "Arial Narrow", sans-serif;
    color: var(--lime);
  }
  .brand-block {
    position: absolute;
    left: 290px;
    top: 76px;
    width: 584px;
    height: 586px;
    background: var(--mark-tone);
  }
  .services {
    position: absolute;
    left: 272px;
    top: 118px;
  }
  .services-title {
    margin-left: 46px;
    font-weight: 700;
    font-size: 24px;
    letter-spacing: 0.3px;
    line-height: 34px;
  }
  .service-list { list-style: none; }
  .service-item {
    display: flex;
    align-items: center;
    height: 34.7px;
    font-size: 26px;
    font-weight: 400;
    letter-spacing: 0.4px;
  }
  .service-icon {
    width: 22px;
    height: 22px;
    margin-right: 24px;
    flex: none;
  }
  .builders-note,
  .thanks-note {
    position: absolute;
    left: 0;
    width: 1200px;
    text-align: center;
    font-size: 30px;
    font-weight: 400;
    letter-spacing: 0.4px;
  }
  .builders-note { top: 480px; }
  .thanks-note { top: 602px; }
</style>
</head>
<body>
<main class="card-back">
  <div class="brand-block" aria-hidden="true"></div>

  <section class="services">
    <h2 class="services-title">Services offered (but not limited to) include:</h2>
    <ul class="service-list">
      <li class="service-item"><svg class="service-icon" viewBox="0 0 22 22" aria-hidden="true"><circle cx="11" cy="11" r="10" fill="var(--lime)"/><path d="M5 11.5 L10 9.5 L11 12 L17 10" fill="none" stroke="var(--ink)" stroke-width="1.6"/></svg>Domestic, commercial and industrial works</li>
      <li class="service-item"><svg class="service-icon" viewBox="0 0 22 22" aria-hidden="true"><circle cx="11" cy="11" r="10" fill="var(--lime)"/><path d="M5 11.5 L10 9.5 L11 12 L17 10" fill="none" stroke="var(--ink)" stroke-width="1.6"/></svg>New home or renovation wiring</li>
      <li class="service-item"><svg class="service-icon" viewBox="0 0 22 22" aria-hidden="true"><circle cx="11" cy="11" r="10" fill="var(--lime)"/><path d="M5 11.5 L10 9.5 L11 12 L17 10" fill="none" stroke="var(--ink)" stroke-width="1.6"/></svg>Real estate and commercial maintenance</li>
      <li class="service-item"><svg class="service-icon" viewBox="0 0 22 22" aria-hidden="true"><circle cx="11" cy="11" r="10" fill="var(--lime)"/><path d="M5 11.5 L10 9.5 L11 12 L17 10" fill="none" stroke="var(--ink)" stroke-width="1.6"/></svg>Spilt system air conditioning</li>
      <li class="service-item"><svg class="service-icon" viewBox="0 0 22 22" aria-hidden="true"><circle cx="11" cy="11" r="10" fill="var(--lime)"/><path d="M5 11.5 L10 9.5 L11 12 L17 10" fill="none" stroke="var(--ink)" stroke-width="1.6"/></svg>Phone TV data</li>
      <li class="service-item"><svg class="service-icon" viewBox="0 0 22 22" aria-hidden="true"><circle cx="11" cy="11" r="10" fill="var(--lime)"/><path d="M5 11.5 L10 9.5 L11 12 L17 10" fill="none" stroke="var(--ink)" stroke-width="1.6"/></svg>Switchboard upgrades</li>
      <li class="service-item"><svg class="service-icon" viewBox="0 0 22 22" aria-hidden="true"><circle cx="11" cy="11" r="10" fill="var(--lime)"/><path d="M5 11.5 L10 9.5 L11 12 L17 10" fill="none" stroke="var(--ink)" stroke-width="1.6"/></svg>Floor heat</li>
    </ul>
  </section>

  <p class="builders-note">Builders welcome</p>
  <p class="thanks-note">Thank you for your business.</p>
</main>
</body>
</html>
```